1 Home page redesign for existing repair service site.

We need a refresh of our existing website that looks more 2017. We have made a mockup of the content that we want and a sample of where we want it. Nothing is set in stone, if you have better ideas of where things should go, feel free.

You can see our current site at http://www.tokelmo.gr

The colors should stay orange/black/grey.

In many of the "boxes/banners" we will need images. Feel free to find in glade barn as we have an account.

We have made notes throughout the wireframe that we have attached on what we are looking for. Let us know if you have any questions. Thanks.

Target Market(s)

People using technology and breaking it

Industry/Entity Type

It Service

Number of Pages Required

1 page

Font styles to use
Sans Serif

Requirements
Must have
• Must have a modern, professional look and feel. Need custom graphics and icons.

```html
<!DOCTYPE html>
<html lang="en">
<head>
<meta charset="utf-8">
<title>Tokelmo – Device Repair</title>
<link href="https://fonts.googleapis.com/css2?family=Open+Sans:ital,wght@0,400;0,600;0,700;1,400&display=swap" rel="stylesheet">
<style>
:root{
  --orange:#ee7d2b;
  --orange-dark:#d96a1c;
  --black:#1d1d1d;
  --charcoal:#3d3d3d;
  --grey:#555;
  --grey-mid:#8a8a8a;
  --grey-light:#f2f1f1;
  --line:#dedede;
  --white:#fff;
}
*{box-sizing:border-box;margin:0;padding:0}
html,body{width:1200px;height:3797px;overflow:hidden}
body{font-family:"Open Sans",Arial,sans-serif;color:var(--grey);background:var(--white);position:relative}
.abs{position:absolute}
a{color:inherit;text-decoration:none}

/* top bar */
.topbar{top:0;left:0;width:1200px;height:46px;background:var(--black);color:#ddd;font-size:13px}
.quick-toggle{left:99px;top:0;width:186px;height:46px;background:#2d2d2d;display:flex;align-items:center;padding-left:48px;gap:28px;font-weight:600;color:#eee}
.lang{left:808px;top:15px;font-size:12px;color:#bbb}
.lang b{color:#fff;font-weight:600;margin-left:6px}
.socials{left:885px;top:15px;display:flex;gap:12px}
.socials i{display:block;width:15px;height:15px;border-radius:50%;background:#cfcfcf}

/* header */
.header{top:46px;left:0;width:1200px;height:86px;background:var(--white);border-bottom:1px solid var(--line)}
.brand{left:99px;top:26px;display:flex;align-items:center;gap:10px;font-size:30px;font-weight:700;color:var(--black)}
.brand i{width:34px;height:34px;background:var(--orange);border-radius:6px;display:block}
.nav{left:312px;top:0;height:86px;display:flex}
.nav a{display:flex;align-items:center;gap:8px;padding:0 38px;height:86px;border-left:1px solid var(--line);font-size:13px;font-weight:600;color:var(--charcoal);text-transform:uppercase}
.nav a:last-child{border-right:1px solid var(--line)}
.call{left:836px;top:20px;display:flex;align-items:center;gap:14px;font-size:20px;font-weight:700;color:var(--black)}
.call span.ic{width:46px;height:46px;background:var(--orange);border-radius:4px;display:flex;align-items:center;justify-content:center}
.chat-btn{left:1023px;top:24px;width:78px;height:38px;border:2px solid var(--black);border-radius:6px;display:flex;align-items:center;justify-content:center;font-size:14px;font-weight:700;color:var(--black)}

/* hero */
.hero{top:132px;left:0;width:1200px;height:496px;background:linear-gradient(160deg,#3a4553 0%,#27303b 45%,#48525c 100%)}
.hero h1{position:absolute;top:170px;width:100%;text-align:center;color:var(--white);font-size:46px;font-weight:700;letter-spacing:1px}
.play{left:572px;top:264px;width:56px;height:56px;border:3px solid #fff;border-radius:50%}
.play:after{content:"";position:absolute;left:20px;top:14px;border-left:18px solid #fff;border-top:11px solid transparent;border-bottom:11px solid transparent}

.counter{top:628px;left:0;width:1200px;height:61px;background:var(--grey-light);display:flex;align-items:center;padding-left:99px;gap:6px;font-size:15px}
.counter .digit{width:22px;height:30px;background:#cfcfcf;border-radius:3px;display:flex;align-items:center;justify-content:center;font-weight:700;color:var(--charcoal)}
.counter p{margin-left:20px;color:var(--grey)}

/* promos */
.promo{top:760px;height:273px;width:486px;color:var(--white)}
.promo.stores{left:99px;background:linear-gradient(90deg,#2e2f31,#4a4b4d)}
.promo.price{left:615px;background:linear-gradient(90deg,#6c6865,#9b9793)}
.promo h3{font-size:24px;font-weight:600;text-transform:uppercase}
.promo .sub{font-size:15px;margin-top:10px}
.promo .more{font-size:15px;font-weight:600}
.stores .txt{position:absolute;left:26px;top:48px}
.stores .more{position:absolute;left:26px;top:198px}
.stores .visual{position:absolute;left:252px;top:92px;width:200px;height:181px;background:linear-gradient(120deg,#c9a489,#e3c6ae);border-radius:4px}
.price .txt{position:absolute;left:0;top:48px;width:340px;text-align:center;left:70px}
.price .more{position:absolute;left:190px;top:200px}
.price .visual{position:absolute;right:0;top:0;width:120px;height:273px;background:linear-gradient(90deg,rgba(0,0,0,0),rgba(230,200,180,.35))}

.rule{left:0;width:1200px;height:3px;background:var(--orange)}

/* feature cards */
.card{top:1177px;width:230px}
.card .ph{height:216px}
.card h4{margin-top:30px;font-size:12px;font-weight:700;color:var(--black);text-transform:uppercase}
.card p{margin-top:8px;font-size:12px;line-height:1.55;height:38px}
.card .rm{display:block;margin-top:14px;font-size:11px;font-weight:700;color:var(--orange);text-transform:uppercase}

/* what we repair */
.repair{top:1588px;left:0;width:1200px;height:562px;background:#f4f3f3}
.sec-title{position:absolute;width:100%;text-align:center;font-size:29px;font-weight:600;color:var(--black)}
.grid{left:99px;top:154px;width:1002px;display:grid;grid-template-columns:repeat(5,1fr);border-top:1px solid var(--line);border-left:1px solid var(--line)}
.grid div{height:163px;border-right:1px solid var(--line);border-bottom:1px solid var(--line);display:flex;flex-direction:column;align-items:center;justify-content:center;gap:20px;font-size:15px;color:var(--charcoal)}
.grid svg{height:60px}

/* options */
.options{top:2289px;left:99px;width:1002px;height:106px;display:flex;box-shadow:0 14px 16px -10px rgba(0,0,0,.35)}
.options div{flex:1;background:#3f3f3f;color:#fff;display:flex;flex-direction:column;align-items:center;justify-content:center;gap:14px;font-size:13px;font-weight:700;text-transform:uppercase}
.options div.active{background:var(--orange)}

/* why choose */
.why{top:2610px;width:231px;height:231px;background:var(--orange);color:#fff;display:flex;flex-direction:column;align-items:center;padding-top:58px;font-size:13px;font-weight:700;text-transform:uppercase}
.why .ring{width:74px;height:74px;border:2px solid #fff;border-radius:50%;display:flex;align-items:center;justify-content:center;margin-bottom:46px}
.why.first:after{content:"";position:absolute;left:104px;bottom:-14px;border-top:14px solid var(--orange);border-left:12px solid transparent;border-right:12px solid transparent}
.arrow{top:2710px;font-size:26px;color:var(--charcoal)}

/* testimonial */
.testi{top:2912px;left:0;width:1200px;height:220px;background:#f4f3f3}
.avatar{left:152px;top:50px;width:114px;height:114px;border-radius:50%;background:linear-gradient(#c8b5a3,#8f7a68);border:4px solid #fff}
.quote{left:299px;top:52px;width:800px;font-size:13px;font-style:italic;line-height:1.75;color:var(--grey)}
.quote b{display:block;margin-top:12px;font-weight:700;color:var(--black)}
.t-nav{left:1000px;top:128px;color:var(--orange);font-size:22px;letter-spacing:18px}

/* footer */
.f-col{top:3200px}
.f-col h5{font-size:14px;font-weight:700;color:var(--black);text-transform:uppercase;margin-bottom:20px}
.f-links li{list-style:none;font-size:12px;line-height:31px}
.f-links li:before{content:"›";color:var(--orange);margin-right:10px}
.post{display:flex;align-items:center;gap:16px;margin-bottom:30px}
.post .date{width:54px;height:54px;border-radius:50%;background:#ddd;font-size:11px;text-align:center;display:flex;align-items:center;justify-content:center;line-height:1.3;color:var(--charcoal)}
.post .box{width:285px;border:1px solid var(--line);padding:10px 12px;font-size:12px;line-height:1.5}
.news p{font-size:12px;margin-bottom:14px}
.news .input{width:272px;height:40px;border:1px solid var(--line);font-size:11px;padding:12px;color:#999}
.news .btn{margin-top:12px;width:102px;height:40px;background:var(--orange);color:#fff;font-size:11px;font-weight:700;display:flex;align-items:center;justify-content:center;text-transform:uppercase}
.news h5.social{margin-top:28px;margin-bottom:14px}
.news .row{display:flex;gap:12px}
.news .row i{display:block;width:15px;height:15px;border-radius:50%;background:var(--grey)}

.help{top:3567px;left:99px;font-size:15px;font-weight:700;color:var(--black);text-transform:uppercase}
.contact{top:3633px;display:flex;gap:20px}
.contact .ci{width:62px;height:62px;border:2px solid var(--orange);border-radius:50%;display:flex;align-items:center;justify-content:center}
.contact h6{font-size:16px;font-weight:600;color:var(--black)}
.contact p{font-size:11px;line-height:1.5;margin-top:4px}
.contact p span{color:var(--orange)}

.bottombar{top:3747px;left:0;width:1200px;height:50px;background:var(--black);color:#ccc;font-size:11px}
.cards{left:99px;top:15px;display:flex;gap:6px}
.cards i{display:block;width:34px;height:20px;background:#e9e9e9;border-radius:2px}
.cards i.wide{width:52px}
.copy{right:96px;top:17px}
</style>
</head>
<body>

<div class="abs topbar">
  <div class="abs quick-toggle">QUICK LINKS <span>&#8964;</span></div>
  <div class="abs lang">GRE <b>ENG</b></div>
  <div class="abs socials"><i></i><i></i><i></i><i></i><i></i><i></i><i></i></div>
</div>

<header class="abs header">
  <div class="abs brand"><i></i>Tokelmo</div>
  <nav class="abs nav">
    <a>Repairs <span>&#8964;</span></a>
    <a>Services <span>&#8964;</span></a>
    <a>20 Stores</a>
    <a>Blog</a>
  </nav>
  <div class="abs call"><span class="ic"><svg width="24" height="24" viewBox="0 0 24 24"><path d="M6.6 10.8a15 15 0 0 0 6.6 6.6l2.2-2.2a1 1 0 0 1 1-.25 11.4 11.4 0 0 0 3.6.6 1 1 0 0 1 1 1V20a1 1 0 0 1-1 1A17 17 0 0 1 3 4a1 1 0 0 1 1-1h3.5a1 1 0 0 1 1 1 11.4 11.4 0 0 0 .6 3.6 1 1 0 0 1-.25 1z" fill="#fff"/></svg></span>2104455120</div>
  <div class="abs chat-btn">Live Chat</div>
</header>

<section class="abs hero" role="img" aria-label="Technician's hands repairing a laptop motherboard on a workbench">
  <h1>WELCOME TO TOKELMO</h1>
  <div class="abs play"></div>
</section>

<div class="abs counter">
  <span class="digit">0</span><span class="digit">1</span><span class="digit">2</span><span class="digit">3</span><span class="digit">4</span>
  <p>Repairs completed with happy customers. Yep,we fix a lot of devices</p>
</div>

<div class="abs promo stores">
  <div class="txt"><h3>20 Tokelmo Locations</h3><p class="sub">FIND A STORE NEAR YOU</p></div>
  <a class="more">View map &gt;</a>
  <div class="visual" role="img" aria-label="Hand holding a phone showing a store map"></div>
</div>
<div class="abs promo price">
  <div class="visual" role="img" aria-label="Woman using a phone"></div>
  <div class="txt"><h3>Low Price Guarantee</h3><p class="sub">Find a lower price for your phone or tablet repair?</p><p class="sub">We will match it!</p></div>
  <a class="more">Read more &gt;&gt;</a>
</div>

<div class="abs rule" style="top:1106px"></div>

<div class="abs card" style="left:99px">
  <div class="ph" role="img" aria-label="Technician explaining a repair to a customer" style="background:linear-gradient(135deg,#6b5d54,#3c3532)"></div>
  <h4>Open Service Area</h4><p>Repairs right in front of you no closed doors, no back rooms</p><a class="rm">Read more &#10148;</a>
</div>
<div class="abs card" style="left:357px">
  <div class="ph" role="img" aria-label="Repair workbench with a laptop" style="background:linear-gradient(135deg,#4d5a5c,#2c3234)"></div>
  <h4>Save 50-75% on multiple repairs</h4><p>If your device needs more than 1 part save up to 75% on additional parts</p><a class="rm">Read more &#10148;</a>
</div>
<div class="abs card" style="left:614px">
  <div class="ph" role="img" aria-label="Phone accessories and a screwdriver on a table" style="background:linear-gradient(135deg,#c9c7c1,#8d8a84)"></div>
  <h4>Accessories</h4><p>Cases, chargers and screen guards for every device we fix daily.</p><a class="rm">Read more &#10148;</a>
</div>
<div class="abs card" style="left:871px">
  <div class="ph" role="img" aria-label="Technician testing a phone circuit board" style="background:linear-gradient(135deg,#7d8a9c,#c3b9b3)"></div>
  <h4>20 Minute Repairs</h4><p>Most repairs can be completed in about 20 minutes.</p><a class="rm">Read more &#10148;</a>
</div>

<section class="abs repair">
  <h2 class="sec-title" style="top:64px">What We Repair</h2>
  <div class="abs grid">
    <div><svg viewBox="0 0 30 60" width="30"><rect x="2" y="2" width="26" height="56" rx="4" fill="none" stroke="#ee7d2b" stroke-width="3"/><line x1="11" y1="52" x2="19" y2="52" stroke="#ee7d2b" stroke-width="3"/></svg>Fonix Repair</div>
    <div><svg viewBox="0 0 48 60" width="48"><rect x="2" y="2" width="44" height="56" rx="4" fill="none" stroke="#ee7d2b" stroke-width="3"/><rect x="8" y="8" width="32" height="40" fill="none" stroke="#ee7d2b" stroke-width="2"/></svg>Tabix Repair</div>
    <div><svg viewBox="0 0 34 60" width="34"><rect x="2" y="2" width="30" height="56" rx="4" fill="none" stroke="#ee7d2b" stroke-width="3"/><rect x="7" y="9" width="20" height="38" fill="none" stroke="#ee7d2b" stroke-width="2"/></svg>Tabix Touch Repair</div>
    <div><svg viewBox="0 0 30 60" width="30"><rect x="2" y="2" width="26" height="56" rx="6" fill="none" stroke="#ee7d2b" stroke-width="3"/><line x1="2" y1="46" x2="28" y2="46" stroke="#ee7d2b" stroke-width="2"/></svg>Solvang Repair</div>
    <div><svg viewBox="0 0 36 60" width="36"><rect x="2" y="2" width="32" height="56" rx="5" fill="#ee7d2b"/><rect x="7" y="8" width="22" height="18" fill="#fff"/><g fill="#fff"><circle cx="11" cy="34" r="2"/><circle cx="18" cy="34" r="2"/><circle cx="25" cy="34" r="2"/><circle cx="11" cy="42" r="2"/><circle cx="18" cy="42" r="2"/><circle cx="25" cy="42" r="2"/></g></svg>Bramble Repair</div>
    <div><svg viewBox="0 0 60 54" width="60"><rect x="2" y="2" width="56" height="38" rx="2" fill="none" stroke="#ee7d2b" stroke-width="3"/><path d="M24 40v8h12v-8M16 50h28" stroke="#ee7d2b" stroke-width="3" fill="none"/></svg>Desko Repairs</div>
    <div><svg viewBox="0 0 66 46" width="66"><rect x="10" y="2" width="46" height="34" rx="2" fill="none" stroke="#ee7d2b" stroke-width="3"/><path d="M2 40h62v3H2z" fill="#ee7d2b"/></svg>Lumabook Repair</div>
    <div><svg viewBox="0 0 66 56" width="66"><rect x="2" y="6" width="42" height="32" fill="none" stroke="#ee7d2b" stroke-width="3"/><path d="M18 38v8M10 48h26" stroke="#ee7d2b" stroke-width="3"/><rect x="50" y="4" width="14" height="48" fill="none" stroke="#ee7d2b" stroke-width="3"/><line x1="53" y1="14" x2="61" y2="14" stroke="#ee7d2b" stroke-width="2"/></svg>Computer Repair</div>
    <div><svg viewBox="0 0 66 46" width="66"><rect x="10" y="4" width="46" height="32" fill="none" stroke="#ee7d2b" stroke-width="3"/><path d="M2 38h62l-4 6H6z" fill="none" stroke="#ee7d2b" stroke-width="3"/></svg>Laptop Repair</div>
    <div><svg viewBox="0 0 56 60" width="56"><circle cx="28" cy="28" r="12" fill="#ee7d2b"/><rect x="22" y="42" width="12" height="10" fill="#ee7d2b"/><g stroke="#ee7d2b" stroke-width="3"><path d="M28 4v7M8 28h7M41 28h7M13 13l5 5M43 13l-5 5"/></g></svg>Business Services</div>
  </div>
</section>

<h2 class="sec-title abs" style="top:2214px">Repair options</h2>
<div class="abs options">
  <div><svg width="52" height="34" viewBox="0 0 52 34"><rect x="2" y="4" width="30" height="20" fill="#fff"/><path d="M32 10h10l8 8v6H32z" fill="#fff"/><circle cx="12" cy="27" r="5" fill="#fff" stroke="#3f3f3f" stroke-width="2"/><circle cx="40" cy="27" r="5" fill="#fff" stroke="#3f3f3f" stroke-width="2"/></svg>Find a store near you?</div>
  <div class="active"><svg width="32" height="38" viewBox="0 0 32 38"><rect x="2" y="12" width="28" height="24" fill="none" stroke="#fff" stroke-width="3"/><path d="M10 14V9a6 6 0 0 1 12 0v5" fill="none" stroke="#fff" stroke-width="3"/></svg>Send us your device?</div>
  <div><svg width="40" height="40" viewBox="0 0 40 40"><path d="M34 14A16 16 0 1 0 36 22" fill="none" stroke="#fff" stroke-width="4"/><circle cx="20" cy="20" r="6" fill="none" stroke="#fff" stroke-width="3"/><path d="M30 4l6 8-10 2z" fill="#fff"/></svg>Free pickup in Athens</div>
</div>

<div class="abs rule" style="top:2468px"></div>

<h2 class="sec-title abs" style="top:2518px">Why Choose Tokelmo</h2>
<div class="abs arrow" style="left:60px">&#8249;</div>
<div class="abs arrow" style="left:1126px">&#8250;</div>
<div class="abs why first" style="left:99px"><span class="ring" style="font-size:20px">24</span>20 Minutes Repairs</div>
<div class="abs why" style="left:355px"><span class="ring"><svg width="30" height="30" viewBox="0 0 30 30"><rect x="3" y="7" width="24" height="20" rx="2" fill="#fff"/><text x="15" y="23" text-anchor="middle" font-size="14" font-weight="700" fill="#ee7d2b" font-family="Open Sans, sans-serif">&#8364;</text></svg></span>Lowest Prices</div>
<div class="abs why" style="left:613px"><span class="ring"><svg width="28" height="32" viewBox="0 0 28 32"><path d="M14 2l12 4v10c0 8-6 13-12 14C8 29 2 24 2 16V6z" fill="#fff"/><path d="M9 16l4 4 7-8" stroke="#ee7d2b" stroke-width="3" fill="none"/></svg></span>Lifetime Guarantee</div>
<div class="abs why" style="left:871px"><span class="ring"><svg width="32" height="32" viewBox="0 0 32 32"><rect x="8" y="8" width="16" height="16" fill="#fff"/><g stroke="#fff" stroke-width="2"><path d="M12 2v6M16 2v6M20 2v6M12 24v6M16 24v6M20 24v6M2 12h6M2 16h6M2 20h6M24 12h6M24 16h6M24 20h6"/></g></svg></span>Chip Level Repairs</div>

<section class="abs testi">
  <div class="abs avatar" role="img" aria-label="Customer portrait"></div>
  <p class="abs quote">For months my laptop was in meltdown mode. It was terribly slow and I was getting error messages and frequent shutdowns. Since my whole life is on it I was desperate for a better solution because I didn't want to say goodbye to my laptop or my files. Tokelmo saved all my precious files and now my computer is really fast! I recommend them without any hesitation. You guys are fantastic!<b>Eleni P., Marousi</b></p>
  <div class="abs t-nav">&#8249;&#8250;</div>
</section>

<div class="abs f-col" style="left:99px">
  <h5>Quick Links</h5>
  <ul class="f-links">
    <li>About Tokelmo</li><li>Business Services</li><li>Schedule a Pickup</li><li>Job openings</li><li>Shipping Instructions</li><li>Privacy policy</li><li>Send your device with ParcelNest</li>
  </ul>
</div>
<div class="abs f-col" style="left:387px">
  <h5>Tokelmo Blog</h5>
  <div class="post"><span class="date">18/02<br>2017</span><div class="box">Franchise Business: Tokelmo CEO, Marcus Delaney</div></div>
  <div class="post"><span class="date">03/03<br>2017</span><div class="box">81 year old woman learns programming from scratch and creates an app</div></div>
</div>
<div class="abs f-col news" style="left:828px">
  <h5>Sign up to newsletter</h5>
  <p>Get our repair tips and offers.</p>
  <div class="input">Enter Name</div>
  <div class="btn">Subscribe</div>
  <h5 class="social">We're Social</h5>
  <div class="row"><i></i><i></i><i></i><i></i><i></i><i></i><i></i></div>
</div>

<div class="abs" style="top:3514px;left:0;width:1200px;height:1px;background:var(--line)"></div>
<div class="abs help">Can't find what you need?</div>
<div class="abs contact" style="left:99px">
  <span class="ci"><svg width="26" height="20" viewBox="0 0 26 20"><rect x="1" y="1" width="24" height="18" fill="none" stroke="#ee7d2b" stroke-width="2"/><path d="M1 1l12 10L25 1" fill="none" stroke="#ee7d2b" stroke-width="2"/></svg></span>
  <div><h6>Email Support</h6><p>We usually respond within 24 hours.<br><span>Click to send email</span></p></div>
</div>
<div class="abs contact" style="left:440px">
  <span class="ci"><svg width="26" height="26" viewBox="0 0 24 24"><path d="M6.6 10.8a15 15 0 0 0 6.6 6.6l2.2-2.2a1 1 0 0 1 1-.25 11.4 11.4 0 0 0 3.6.6 1 1 0 0 1 1 1V20a1 1 0 0 1-1 1A17 17 0 0 1 3 4a1 1 0 0 1 1-1h3.5a1 1 0 0 1 1 1 11.4 11.4 0 0 0 .6 3.6 1 1 0 0 1-.25 1z" fill="#ee7d2b"/></svg></span>
  <div><h6>Contact our call center</h6><p>Call to speak to a customer service rep.<br><span>210.445.5120</span></p></div>
</div>
<div class="abs contact" style="left:800px">
  <span class="ci"><svg width="28" height="24" viewBox="0 0 28 24"><path d="M2 2h24v15H10l-6 5v-5H2z" fill="none" stroke="#ee7d2b" stroke-width="2"/></svg></span>
  <div><h6>Live Chat</h6><p>Chat with a Tokelmo technician now.<br><span>Click to chat</span></p></div>
</div>

<footer class="abs bottombar">
  <div class="abs cards"><i></i><i></i><i></i><i class="wide"></i></div>
  <div class="abs copy">Copyright &copy; Tokelmo 2017. All rights reserved.</div>
</footer>

</body>
</html>
```